Business cards for a high-end menswear store

I would like to come up with a design for our business cards.
Two different ones: one for general sales and one for the owner. It is a high-end menswear store.

Our address is: 4817 Valmonde Boulevard, Montreal, QC, H2R4K7
phone number: 514-582-3960
insta: MAISONVERLAINT
Website: www.maisonverlaint.com
email (general card): info@maisonverlaint.com
email (owner): morvin@maisonverlaint.com

I have attached our logo in an ai and eps file format. You can see our old cards as well. I am looking for a modern and clean look.

Target Market(s)

High-End Clothing Market

Industry/Entity Type

Retail, Clothing, Luxury Clothing

Contact Information for Business Card

Address, Name, Email, Website, Social Info,

Font styles to use
Serif

Colors

Designer to choose colors to be used in the design.

Requirements
Must have
• Address, Name, Email, Website, Social Info,
Nice to have
• QR Code that brings you to the website

```html
<!DOCTYPE html>
<html lang="en">
<head>
<meta charset="utf-8">
<title>Maison Verlaint — Business Cards</title>
<link href="https://fonts.googleapis.com/css2?family=Montserrat:wght@400&display=swap" rel="stylesheet">
<style>
  :root {
    --backdrop: #e9e9eb;
    --card-black: #221f20;
    --ink-white: #ffffff;
    --shadow: rgba(0, 0, 0, 0.18);
  }
  * { margin: 0; padding: 0; box-sizing: border-box; }
  html, body {
    width: 1200px;
    height: 900px;
    overflow: hidden;
    background: var(--backdrop);
    font-family: "Montserrat", sans-serif;
    color: var(--ink-white);
  }
  .canvas { position: relative; width: 1200px; height: 900px; }

  .card {
    position: absolute;
    width: 700px;
    height: 400px;
    background: var(--card-black);
    box-shadow: 0 10px 30px var(--shadow);
  }
  .card--front { left: 110px; top: 35px; }
  .card--back  { left: 390px; top: 465px; }

  .brand-name {
    position: absolute;
    text-align: left;
    font-weight: 400;
    color: var(--ink-white);
    line-height: 1;
  }
  .brand-name__top {
    display: block;
    font-size: 15px;
    letter-spacing: 0.62em;
    margin-bottom: 12px;
  }
  .brand-name__main {
    display: block;
    font-size: 44px;
    letter-spacing: 0.08em;
  }
  .card--front .brand-name { left: 230px; top: 160px; }
  .card--back  .brand-name { right: 56px; top: 58px; }

  .contact-list {
    position: absolute;
    left: 52px;
    list-style: none;
    font-size: 17px;
    letter-spacing: 0.02em;
  }
  .contact-list--place { top: 200px; }
  .contact-list--reach { top: 282px; }
  .contact-item {
    display: flex;
    align-items: flex-start;
    gap: 12px;
    line-height: 22px;
  }
  .contact-item + .contact-item { margin-top: 3px; }
  .contact-list--place .contact-item + .contact-item { margin-top: 6px; }
  .contact-icon {
    flex: 0 0 18px;
    width: 18px;
    height: 18px;
    margin-top: 2px;
    fill: var(--ink-white);
  }
  .social-dot {
    flex: 0 0 18px;
    width: 18px;
    height: 18px;
    margin-top: 2px;
    border-radius: 50%;
    background: var(--ink-white);
  }
</style>
</head>
<body>
<main class="canvas">

  <section class="card card--front" aria-label="Card front">
    <div class="brand-name">
      <span class="brand-name__top">MAISON</span>
      <span class="brand-name__main">VERLAINT</span>
    </div>
  </section>

  <section class="card card--back" aria-label="Card back">
    <div class="brand-name">
      <span class="brand-name__top">MAISON</span>
      <span class="brand-name__main">VERLAINT</span>
    </div>

    <ul class="contact-list contact-list--place">
      <li class="contact-item">
        <span class="social-dot" aria-hidden="true"></span>
        <span>MAISONVERLAINT</span>
      </li>
      <li class="contact-item">
        <svg class="contact-icon" viewBox="0 0 24 24" aria-hidden="true">
          <path d="M12 1.5a7.5 7.5 0 0 0-7.5 7.5c0 5.6 7.5 13.5 7.5 13.5s7.5-7.9 7.5-13.5A7.5 7.5 0 0 0 12 1.5zm0 10.5a3 3 0 1 1 0-6 3 3 0 0 1 0 6z"/>
        </svg>
        <span>4817 Valmonde Boulevard<br>Montreal, QC, H2R4K7</span>
      </li>
    </ul>

    <ul class="contact-list contact-list--reach">
      <li class="contact-item">
        <svg class="contact-icon" viewBox="0 0 24 24" aria-hidden="true">
          <path d="M6.6 10.8a15.1 15.1 0 0 0 6.6 6.6l2.2-2.2a1 1 0 0 1 1-.25 11.4 11.4 0 0 0 3.6.57 1 1 0 0 1 1 1V20a1 1 0 0 1-1 1A17 17 0 0 1 3 4a1 1 0 0 1 1-1h3.5a1 1 0 0 1 1 1c0 1.25.2 2.45.57 3.57a1 1 0 0 1-.25 1z"/>
        </svg>
        <span>514-582-3960</span>
      </li>
      <li class="contact-item">
        <svg class="contact-icon" viewBox="0 0 24 24" aria-hidden="true">
          <path d="M2 5h20v14H2z" fill="none" stroke="#fff" stroke-width="2"/>
          <path d="M2 5l10 8 10-8" fill="none" stroke="#fff" stroke-width="2"/>
        </svg>
        <span>info@maisonverlaint.com</span>
      </li>
      <li class="contact-item">
        <svg class="contact-icon" viewBox="0 0 24 24" aria-hidden="true">
          <path d="M2 5h20v14H2z" fill="none" stroke="#fff" stroke-width="2"/>
          <path d="M2 5l10 8 10-8" fill="none" stroke="#fff" stroke-width="2"/>
        </svg>
        <span>morvin@maisonverlaint.com</span>
      </li>
      <li class="contact-item">
        <svg class="contact-icon" viewBox="0 0 24 24" aria-hidden="true">
          <circle cx="12" cy="12" r="9.5" fill="none" stroke="#fff" stroke-width="2"/>
          <ellipse cx="12" cy="12" rx="4" ry="9.5" fill="none" stroke="#fff" stroke-width="1.6"/>
          <path d="M2.5 12h19" stroke="#fff" stroke-width="1.6"/>
        </svg>
        <span>www.maisonverlaint.com</span>
      </li>
    </ul>
  </section>

</main>
</body>
</html>
```